Mobile Club Table Tent

BrivoSend provides a mobile marketing and communications platform for churches, restaurants, bars and retail stores. The heart of the BrivoSend platform is a private Mobile Club for each business or organization. I need to design a 'Join our Mobile Club' table tent for The Copper Kettle Bar and Grill.

I would like the table tent to include a flat design and basic color scheme from our website at www.brivosend-example.com

Size: 4.25" x 6" (4.25x6_table_tent_511.psd template provided)

Table Tent Front Text:
Join Our Mobile Club

Join our Mobile Club for daily, weekly or monthly updates from The Copper Kettle Bar and Grill.

(insert The Copper Kettle Bar and Grill logo)

-Free Membership
-Exclusive Mobile Club Specials
-Invitations to Mobile Club Events
-Unlock Deals and RSVP for Events

Table Tent Back Text:
Connect with The Copper Kettle Bar and Grill on your phone, desktop or tablet.

(place image of desktop, table and smart phone with screens from http://copperkettle.pageweave-example.com/)

1.) Call to Join (insert phone icon image)
Call (555) 284-7716 to access our Mobile Club Sign Up Menu.
or

2.) Text to Join (insert SMS icon image)
Text 'JOIN' to (555) 284-7716 and Join our Mobile Club by text message.
or

3.) Scan to Join (insert QR code)
Scan the QR code and Join our Mobile Club by Email or Text Message.
or

4.) Ask your server for more information.

Also include the following text on either front, back or bottom of Table Tent.

The Copper Kettle Bar and Grill
4827 N. Fable Lane
Littleton CO 80000
(555) 610-3392
contact@copperkettlegrill-example.com

Standard Text Message Charges May Apply.
You can update your profile, take control of your inbox or Opt-out at any time.
Mobile Club powered by BrivoSend.

I have also updated example designs for reference only.

```html
<!DOCTYPE html>
<html lang="en">
<head>
<meta charset="utf-8">
<title>Join Our Mobile Club – The Copper Kettle Bar and Grill</title>
<link rel="stylesheet" href="https://fonts.googleapis.com/css2?family=Delius&display=swap">
<style>
  :root {
    --wood-frame: #4e2a17;
    --frame-trim: #f2e39c;
    --panel-grey: #9e958c;
    --ribbon-tail: #4a1426;
    --ribbon-face: #8c6569;
    --ribbon-edge: #ffffff;
    --title-green: #4f6249;
    --title-outline: #2b3326;
    --seal-maroon: #5c1a36;
    --seal-gold: #f2cf2c;
    --body-text: #f5eedc;
    --page-bg: #ffffff;
  }
  * { box-sizing: border-box; }
  html, body {
    margin: 0;
    padding: 0;
    width: 850px;
    height: 1200px;
    overflow: hidden;
    background: var(--page-bg);
  }
  .table-tent {
    position: relative;
    width: 850px;
    height: 1200px;
    background: var(--wood-frame);
    font-family: "Delius", "Trebuchet MS", sans-serif;
  }
  .panel {
    position: absolute;
    left: 18px;
    top: 18px;
    width: 814px;
    height: 1164px;
    border: 6px solid var(--frame-trim);
    background: var(--panel-grey);
  }
  .banner {
    position: absolute;
    left: 0;
    top: 0;
    width: 850px;
    height: 200px;
  }
  .banner-label {
    font-family: "Delius", "Trebuchet MS", sans-serif;
    font-size: 78px;
    fill: var(--ribbon-edge);
    letter-spacing: 2px;
  }
  .club-title {
    position: absolute;
    left: 0;
    top: 192px;
    width: 850px;
    margin: 0;
    text-align: center;
    font-size: 104px;
    font-weight: 400;
    line-height: 1;
    letter-spacing: 4px;
    color: var(--title-green);
    -webkit-text-stroke: 3px var(--title-outline);
  }
  .brand-seal {
    position: absolute;
    left: 195px;
    top: 345px;
    width: 460px;
    height: 460px;
    border-radius: 50%;
    background: var(--seal-maroon);
    display: flex;
    align-items: center;
    justify-content: center;
    text-align: center;
  }
  .brand-name {
    margin: 0;
    font-size: 64px;
    font-weight: 400;
    line-height: 1.1;
    color: var(--seal-gold);
  }
  .intro {
    position: absolute;
    left: 0;
    top: 884px;
    width: 850px;
    margin: 0;
    text-align: center;
    font-size: 29px;
    line-height: 40px;
    color: var(--body-text);
  }
  .perks {
    position: absolute;
    left: 0;
    top: 978px;
    width: 850px;
    margin: 0;
    padding: 0;
    list-style: none;
    text-align: center;
    font-size: 24px;
    line-height: 33px;
    color: var(--body-text);
  }
</style>
</head>
<body>
  <main class="table-tent">
    <div class="panel"></div>

    <svg class="banner" viewBox="0 0 850 200" aria-hidden="false" role="img" aria-label="Join our">
      <polygon points="112,55 200,55 200,175 112,175 150,115" fill="var(--ribbon-tail)" stroke="var(--ribbon-edge)" stroke-width="4"/>
      <polygon points="738,55 650,55 650,175 738,175 700,115" fill="var(--ribbon-tail)" stroke="var(--ribbon-edge)" stroke-width="4"/>
      <polygon points="112,55 200,55 200,190" fill="var(--ribbon-tail)"/>
      <rect x="140" y="14" width="572" height="108" rx="22" fill="var(--ribbon-face)" stroke="var(--ribbon-edge)" stroke-width="5"/>
      <text class="banner-label" x="425" y="96" text-anchor="middle">JOIN OUR</text>
    </svg>

    <h1 class="club-title">MOBILE CLUB</h1>

    <div class="brand-seal">
      <p class="brand-name">The Copper<br>Kettle</p>
    </div>

    <p class="intro">Join our Mobile Club for daily, weekly or monthly<br>updates from The Copper Kettle Bar and Grill</p>

    <ul class="perks">
      <li>-Free Membership-</li>
      <li>-Exclusive Mobile Club Specials-</li>
      <li>-Invitations to Mobile Club Events-</li>
      <li>-Unlock Deals and RSVP for Events-</li>
    </ul>
  </main>
</body>
</html>
```